Bref créative
FXK-TWO Business Cards and Stationery
Paintless Dent Repair
Modern
Calvin t Moss
Owner-Technician
4172 Salvia ln
riverside ca 91734
glowmenderfxk7@mailvista.example
repair dings dents hail damage
20 years experience master craftsman

```html
<!DOCTYPE html>
<html lang="en">
<head>
<meta charset="utf-8">
<title>FXK-TWO Business Cards</title>
<link rel="stylesheet" href="https://fonts.googleapis.com/css2?family=Russo+One&family=Ubuntu:wght@400;500;700&display=swap">
<style>
  :root {
    --navy: #1c2a57;
    --red: #d4212a;
    --white: #ffffff;
    --ink: #3a3a3a;
    --backdrop: #2b2b2d;
  }
  * { margin: 0; padding: 0; box-sizing: border-box; }
  html, body { width: 1200px; height: 901px; overflow: hidden; }
  body {
    background: var(--backdrop);
    position: relative;
    font-family: "Ubuntu", sans-serif;
  }
  .card {
    position: absolute;
    width: 540px;
    height: 309px;
    border-radius: 18px;
    overflow: hidden;
  }
  .card-back {
    left: 40px; top: 296px;
    background: var(--navy);
    display: flex;
    flex-direction: column;
    align-items: center;
    justify-content: center;
  }
  .brand-name {
    font-family: "Russo One", sans-serif;
    color: var(--red);
    letter-spacing: 1px;
    line-height: 1;
  }
  .card-back .brand-name { font-size: 78px; }
  .tagline {
    display: flex;
    align-items: center;
    gap: 10px;
    font-weight: 500;
    letter-spacing: 2px;
  }
  .tagline::before, .tagline::after {
    content: "";
    display: block;
    height: 2px;
    background: var(--red);
  }
  .card-back .tagline { color: var(--white); font-size: 26px; margin-top: 10px; }
  .card-back .tagline::before, .card-back .tagline::after { width: 34px; }

  .card-front { left: 620px; top: 296px; background: var(--white); }
  .card-front .bands { position: absolute; inset: 0; }
  .card-front .logo-block { position: absolute; left: 30px; top: 30px; }
  .card-front .brand-name { font-size: 40px; }
  .card-front .tagline { color: var(--navy); font-size: 13px; margin-top: 4px; gap: 6px; }
  .card-front .tagline::before, .card-front .tagline::after { width: 16px; }
  .contact {
    position: absolute; left: 40px; top: 150px;
    list-style: none;
    color: var(--ink);
    font-size: 14px;
    line-height: 1.25;
  }
  .contact li { display: flex; align-items: center; gap: 8px; }
  .contact .address { display: block; margin-bottom: 12px; }
  .contact li + li { margin-top: 4px; }
  .contact svg { flex: none; }
  .owner {
    position: absolute; left: 342px; top: 226px;
    white-space: nowrap;
  }
  .owner-name { color: var(--red); font-size: 16px; font-weight: 500; }
  .owner-title { color: var(--white); font-size: 13px; margin-top: 3px; }
</style>
</head>
<body>
  <section class="card card-back">
    <div class="brand-name">FXK-TWO</div>
    <div class="tagline">Paintless dent repair</div>
  </section>

  <section class="card card-front">
    <svg class="bands" width="540" height="309" viewBox="0 0 540 309" aria-hidden="true">
      <polygon points="330,0 540,0 540,309 330,309" fill="var(--navy)"/>
      <polygon points="512,0 540,0 540,309 474,309" fill="var(--red)"/>
    </svg>
    <div class="logo-block">
      <div class="brand-name">FXK-TWO</div>
      <div class="tagline">Paintless dent repair</div>
    </div>
    <ul class="contact">
      <li class="address">4172 Salvia ln<br>riverside ca 91734</li>
      <li>
        <svg width="12" height="14" viewBox="0 0 12 14" aria-hidden="true"><rect x="1.5" y="1" width="9" height="12" rx="1.5" fill="none" stroke="var(--red)" stroke-width="1.6"/><rect x="5" y="10" width="2" height="1.5" fill="var(--red)"/></svg>
        951-555-0142
      </li>
      <li>
        <svg width="12" height="10" viewBox="0 0 12 10" aria-hidden="true"><rect x="0" y="1" width="12" height="8" rx="1" fill="var(--red)"/><path d="M0.5 1.5 L6 5.5 L11.5 1.5" fill="none" stroke="var(--white)" stroke-width="1"/></svg>
        glowmenderfxk7@mailvista.example
      </li>
    </ul>
    <div class="owner">
      <div class="owner-name">Calvin t Moss</div>
      <div class="owner-title">Owner-Technician</div>
    </div>
  </section>
</body>
</html>
```